Create a "germ free" Poster Design Project

Hi we're a media business who sells advertising space on a unique dispensing device that also sanitizes your hands.

I'm looking for a poster design that highlights the need to sanitize hands which removes 99.9% of germs and also promotes a healthy & clean lifestyle.
(you may want to use kid friendly images of bugs to highlight germs)
Whilst the primary message will be to sanitize your hands the secondary message is also to "use this space" to advertise on.

The poster should be colorful yet simple and not too wordy.

Thanks

Target Market(s)

General cunsumer public but more specifically women and moms

Industry/Entity Type

Advertising

Requirements
Must have
• A central picture (animated or real) to highlight the practice of sanitizing hands (or removing germs)
Perhaps an arrow down to invite consumers to "try it now, its free'
Nice to have
• Referal to our web site: Plorvex.com.au (currently not operational) and email info@plorvex.com.au
Perhaps an image of a baby's hand with a creative tag line.
Should not have
• Nothing too gross looking

```html
<!DOCTYPE html>
<html lang="en">
<head>
<meta charset="utf-8">
<title>Removes 99.9% of Germs – Poster</title>
<link rel="stylesheet" href="https://fonts.googleapis.com/css2?family=Bebas+Neue&family=Montserrat:wght@700&family=Open+Sans:wght@400;600&display=swap">
<style>
  :root {
    --page-bg: #eeeeee;
    --poster-bg: #ffffff;
    --night: #1b1718;
    --magenta: #c8197f;
    --plum: #3a1f33;
    --navy: #264c7b;
    --cream: #f4efd6;
    --gold: #ffcc00;
    --ink: #333333;
    --photo-warm: #f1dfd3;
    --photo-light: #f7f4f2;
  }
  * { margin: 0; padding: 0; box-sizing: border-box; }
  html, body { width: 858px; height: 1200px; overflow: hidden; background: var(--page-bg); }
  .poster {
    position: absolute; left: 19px; top: 19px;
    width: 820px; height: 1162px;
    background: var(--poster-bg); overflow: hidden;
  }
  .poster-shapes { position: absolute; inset: 0; }
  .hero-photo {
    position: absolute; left: 340px; top: 720px; width: 480px; height: 363px;
    background: linear-gradient(180deg, var(--photo-warm) 0%, var(--photo-light) 100%);
  }
  .headline {
    position: absolute; left: 0; width: 100%; text-align: center;
    font-family: "Bebas Neue", sans-serif; font-weight: 400; line-height: 1;
    background: linear-gradient(90deg, var(--cream) 20%, var(--gold) 80%);
    -webkit-background-clip: text; background-clip: text; color: transparent;
  }
  .headline--removes { top: 153px; font-size: 115px; letter-spacing: 7px; }
  .headline--figure { top: 290px; font-size: 153px; letter-spacing: 2px; }
  .headline--germs { top: 452px; font-size: 158px; letter-spacing: 5px; }
  .brand { position: absolute; left: 75px; top: 866px; display: flex; align-items: center; }
  .brand-dot { width: 90px; height: 90px; border-radius: 50%; background: var(--magenta); }
  .brand-name {
    margin-left: 18px; font-family: "Open Sans", sans-serif; font-weight: 600;
    font-size: 36px; color: var(--magenta);
  }
  .contact {
    position: absolute; left: 49px; top: 992px;
    font-family: "Open Sans", sans-serif; font-size: 16px; color: var(--ink);
  }
  .tagline-bar {
    position: absolute; left: 0; top: 1089px; width: 100%; height: 73px;
    background: var(--navy); display: flex; align-items: center; justify-content: center;
    font-family: "Montserrat", sans-serif; font-weight: 700; font-size: 30px;
    letter-spacing: 3px; color: #ffffff;
  }
</style>
</head>
<body>
  <main class="poster">
    <div class="hero-photo" role="img" aria-label="Photo of a child's hand held in an adult's hand, with a magnifying glass showing germs"></div>

    <svg class="poster-shapes" viewBox="0 0 820 1162" width="820" height="1162" aria-hidden="true">
      <defs>
        <linearGradient id="crown" x1="0" x2="1" y1="0" y2="0">
          <stop offset="0" stop-color="#3a1f33"/>
          <stop offset="0.5" stop-color="#c8197f"/>
          <stop offset="1" stop-color="#3a1f33"/>
        </linearGradient>
        <linearGradient id="swoosh" x1="0" x2="1" y1="0" y2="0">
          <stop offset="0" stop-color="#c8197f"/>
          <stop offset="0.55" stop-color="#c8197f"/>
          <stop offset="0.8" stop-color="#264c7b"/>
          <stop offset="1" stop-color="#264c7b"/>
        </linearGradient>
        <linearGradient id="rule" x1="0" x2="1" y1="0" y2="0">
          <stop offset="0" stop-color="#222"/>
          <stop offset="0.5" stop-color="#bbb"/>
          <stop offset="1" stop-color="#222"/>
        </linearGradient>
      </defs>
      <rect class="crown-band" x="0" y="0" width="820" height="120" fill="url(#crown)"/>
      <path class="night-panel" d="M0 87 Q410 10 820 87 L820 752 Q500 660 0 740 Z" fill="var(--night)"/>
      <path class="accent-swoosh" d="M0 740 Q500 660 820 752 L820 772 Q500 690 0 782 Z" fill="url(#swoosh)"/>
      <rect class="base-rule" x="0" y="1081" width="820" height="8" fill="url(#rule)"/>
    </svg>

    <h1>
      <span class="headline headline--removes">REMOVES</span>
      <span class="headline headline--figure">99.9%</span>
      <span class="headline headline--germs">OF GERMS</span>
    </h1>

    <div class="brand">
      <span class="brand-dot"></span>
      <span class="brand-name">Plorvex</span>
    </div>
    <p class="contact">www.Plorvex.com.au | info@plorvex.com.au</p>

    <div class="tagline-bar">HEALTHY &amp; CLEAN LIFESTYLE</div>
  </main>
</body>
</html>
```